A Dedicated Thank You to my Dad

Proposed Dimensions: Approx. 20" x 30"

For Father's Day, I wrote a dedication to my Dad that encapsulates my gratitude for everything he does, and everything he is. His birthday is on August 3, but it is more important for me to transform this dedication into a meaningful and memorable gift than to meet any deadline. I would love an image that captures the relationship between a father and his son, accompanied by my words of thanks in some sort of font that is appropriate for the message (calligprahy? not sure about that).

I had actually posted the Thank You on Pixelmarrow as a public post, so anyone with an account can read it: https://www.pixelmarrow.example/photo.php?fbid=40872219360548813&set=a.318760942157.6650129.3908471&type=1&theater

Only the words starting with "Thank you ..." should be on the poster.

Target Market(s)

This is a personal gift for my Dad. He doesn't have the best of eyesight, so having the words in a really small font would not be particularly helpful. :-)

Requirements
Must have
• * Personable
* Warm
* Inviting
* Memorable
* Understated more favored over Loud
Should not have
• * An entire palette of colors
* Wacky colors or fonts

```html
<!DOCTYPE html>
<html lang="en">
<head>
<meta charset="utf-8">
<title>Dad – A Dedicated Thank You</title>
<link rel="stylesheet" href="https://fonts.googleapis.com/css2?family=Archivo+Black&family=Yesteryear&display=swap">
<style>
  :root {
    --matte: #000000;
    --paper: #ffffff;
    --plum: #3f1450;
    --lavender: #c9b6d6;
    --lavender-soft: #e6dbec;
    --gold-soft: #e8d9a6;
    --ink: #111111;
    --photo-warm: #8a6a55;
    --photo-blue: #9db8d8;
  }
  * { margin: 0; padding: 0; box-sizing: border-box; }
  html, body { width: 900px; height: 1200px; overflow: hidden; background: var(--matte); }
  .canvas { position: relative; width: 900px; height: 1200px; background: var(--matte); }
  .poster {
    position: absolute; left: 102px; top: 77px; width: 698px; height: 1047px;
    background: linear-gradient(180deg, var(--paper) 0%, var(--paper) 55%, var(--lavender-soft) 80%, var(--lavender) 100%);
    overflow: hidden;
  }
  .hands-photo {
    position: absolute; left: 200px; top: 240px; width: 498px; height: 780px;
    background:
      radial-gradient(ellipse at 60% 10%, var(--gold-soft) 0%, rgba(232,217,166,0.4) 30%, transparent 55%),
      radial-gradient(ellipse at 45% 65%, rgba(190,168,210,0.75) 0%, rgba(210,195,225,0.45) 45%, transparent 75%);
    opacity: 0.9;
  }
  .portrait-photo {
    position: absolute; left: 280px; top: 0; width: 418px; height: 270px;
    background: linear-gradient(120deg, var(--photo-warm) 20%, #5b4a44 55%, var(--photo-blue) 85%);
    -webkit-mask-image: radial-gradient(ellipse 95% 100% at 100% 0%, #000 45%, transparent 100%);
    mask-image: radial-gradient(ellipse 95% 100% at 100% 0%, #000 45%, transparent 100%);
    opacity: 0.85;
  }
  .title {
    position: absolute; left: 30px; top: 45px;
    font-family: "Archivo Black", "Arial Black", sans-serif;
    font-size: 150px; line-height: 1; letter-spacing: -2px;
    color: var(--plum);
  }
  .thanks { position: absolute; left: 53px; top: 0; width: 620px; list-style: none; }
  .thanks li {
    position: absolute; left: 0; white-space: nowrap;
    font-family: "Yesteryear", cursive;
    font-size: 17px; line-height: 1; color: var(--ink);
  }
  .signature { color: var(--plum); }
  .car-silhouette {
    position: absolute; left: 42px; top: 926px; width: 288px; height: 88px;
    background: radial-gradient(ellipse 60% 80% at 50% 100%, var(--plum) 0%, rgba(63,20,80,0.75) 55%, rgba(63,20,80,0) 100%);
  }
  .family-silhouette {
    position: absolute; left: 412px; top: 911px; width: 127px; height: 103px;
    background: radial-gradient(ellipse 60% 85% at 50% 100%, var(--plum) 0%, rgba(63,20,80,0.75) 55%, rgba(63,20,80,0) 100%);
  }
  .ground-band { position: absolute; left: 0; bottom: 0; width: 100%; height: 35px; background: var(--plum); }
</style>
</head>
<body>
<div class="canvas">
  <article class="poster">
    <div class="hands-photo" role="img" aria-label="Soft photograph of a father's hand holding a child's hand, tinted gold and lavender"></div>
    <div class="portrait-photo" role="img" aria-label="Photograph of a smiling son with his father's arm around him"></div>
    <h1 class="title">DAD</h1>
    <ul class="thanks">
      <li style="top:233px">Thank you for welcoming more people to stay with us than I can count.</li>
      <li style="top:298px">Thank you for my dry sense of humor. I cherish it.</li>
      <li style="top:364px">Thank you for never giving up on trying to convince me that imperfection is not a failure.</li>
      <li style="top:431px">Thank you for teaching me to try to find the good in everyone.</li>
      <li style="top:497px">Thank you for showing me that there is peace to be found in stillness and quiet.</li>
      <li style="top:563px">Thank you for demonstrating the fun that can be had and the truths that can be gleaned from debate.</li>
      <li style="top:633px">Thank you for accepting me for who I am, no matter who I love, and for helping me to accept myself.</li>
      <li style="top:699px">Thank you for doing whatever you can to help whoever you can, whether friend, family or stranger.</li>
      <li style="top:766px">Thank you for trusting me enough to let your guard down to let me know how you are truly doing.</li>
      <li style="top:827px">Thank you for insisting, year after year, that time with you means more than any gift I could ever purchase.</li>
      <li style="top:858px">That is one lesson, amongst so many, that I will pass down to our next generation. <span class="signature">DAD</span></li>
    </ul>
    <div class="car-silhouette" role="img" aria-label="Silhouette of a classic car"></div>
    <div class="family-silhouette" role="img" aria-label="Silhouette of a father reaching down to a toddler"></div>
    <div class="ground-band"></div>
  </article>
</div>
</body>
</html>
```